Pembly's - Irish Shortbread

Pembly’s Irish Shortbread
We are looking for a Stand-Up Pouch design – (no window no zip) that will have different flavoured all-butter shortbread in the collection. We love vintage and kitsch as a company but do not have to head in that direction. We are font lovers and would happily have a Font Driven Design for packaging. For this project we were thinking about water colours to define the flavours or Graffiti Package Design. We have 6 flavours, they are:
Irish Shortbread - Ginger Shortbread - Espresso Shortbread - Parmesan and Poppy Seed Shortbread - Strawberry Shortbread - Butterscotch Shortbread.
The size of the pouch is 12cm x 17 cm. There needs to be a hanging hole at the top. We have uploaded a couple of images. What we like is the intensity of colour, clarity of flavour and words. This needs to feel familiar yet fresh on the shelf and not merge with other packaging at the supermarket.
We are also fans of 80s Graffiti designs for packaging – see a few attached images.
I have also attached the brand

```html
<!DOCTYPE html>
<html lang="en">
<head>
<meta charset="utf-8">
<title>Pembly's Irish Shortbread – Pouch Front and Back</title>
<link rel="stylesheet" href="https://fonts.googleapis.com/css2?family=Oswald:wght@300;400;500&family=Sedgwick+Ave+Display&family=Playfair+Display:wght@400&family=Roboto:wght@400;700;900&display=swap">
<style>
:root{
  --ink:#4a3840;
  --purple:#9b2390;
  --plum:#7a2470;
  --lemon:#f3e60a;
  --lime:#d9e61e;
  --orange:#f2a21e;
  --leaf:#4fb444;
  --red:#e4212b;
  --magenta:#d8177a;
  --gold:#f9c80c;
  --paper:#ffffff;
  --edge:#d8e6a8;
}
*{margin:0;padding:0;box-sizing:border-box}
html,body{width:1200px;height:827px;overflow:hidden;background:var(--paper)}
.canvas{position:relative;width:1200px;height:827px;background:var(--paper)}
.panel{position:absolute;top:3px;width:574px;height:812px;overflow:hidden;border:1px solid var(--edge);background:var(--paper)}
.panel--front{left:14px}
.panel--back{left:622px}
.wash{position:absolute;inset:0}
.wash--front{
  clip-path:polygon(0 0,100% 0,100% 50%,0 69%);
  background:
    radial-gradient(circle at 8% 45%,rgba(242,120,30,.75),transparent 32%),
    radial-gradient(circle at 95% 4%,rgba(79,180,68,.8),transparent 18%),
    radial-gradient(circle at 45% 55%,#f7f29a,transparent 40%),
    linear-gradient(160deg,var(--orange) 0%,var(--lemon) 30%,var(--lemon) 70%,var(--lime) 100%);
}
.wash--back{
  clip-path:polygon(0 49.6%,100% 36.5%,100% 100%,0 100%);
  background:
    radial-gradient(circle at 100% 50%,rgba(242,140,30,.8),transparent 25%),
    radial-gradient(circle at 5% 98%,rgba(79,180,68,.85),transparent 22%),
    radial-gradient(circle at 50% 60%,#f7f39c,transparent 45%),
    linear-gradient(180deg,var(--lemon),var(--lime));
}
.hang-hole{position:absolute;left:266px;top:24px;width:28px;height:28px;border-radius:50%;background:#000}
.brand{position:absolute;text-align:center;color:var(--ink)}
.brand__name{font-family:'Oswald',sans-serif;font-weight:500;line-height:1}
.brand__tag{font-family:'Roboto',sans-serif;font-weight:700;letter-spacing:.5em;text-transform:none}
.brand--front{left:140px;top:100px;width:300px}
.brand--front .brand__name{font-size:72px}
.brand--front .brand__tag{font-size:10px;margin-top:14px}
.count-banner{position:absolute;left:151px;top:244px;width:270px;height:47px}
.count-banner span{position:absolute;inset:0;display:flex;align-items:center;justify-content:center;font-family:'Oswald',sans-serif;font-weight:400;font-size:25px;color:#fff;letter-spacing:-.3px}
.title{position:absolute;left:138px;width:310px;text-align:center;font-family:'Sedgwick Ave Display',cursive;line-height:1;color:var(--ink)}
.title--top{top:296px;font-size:58px;letter-spacing:-2px}
.title--mid{top:352px;font-size:96px;color:var(--purple);letter-spacing:-3px}
.title--bottom{top:438px;font-size:58px;letter-spacing:-2px}
.claims-wash{position:absolute;left:30px;top:566px;width:240px;height:180px;border-radius:45% 55% 40% 60%/55% 45% 55% 45%;
  background:radial-gradient(circle at 30% 45%,var(--red),transparent 60%),radial-gradient(circle at 65% 40%,var(--magenta),#8a2a5a 90%);transform:rotate(-8deg)}
.claims{position:absolute;left:82px;top:626px;list-style:none;font-family:'Oswald',sans-serif;font-weight:300;font-size:17px;line-height:22px;color:#fff}
.net-weight{position:absolute;left:82px;top:715px;width:67px;height:100px;background:var(--ink);border-radius:14px 14px 0 0;color:#fff;text-align:center;font-family:'Playfair Display',serif;padding-top:8px}
.net-weight small{display:block;font-size:11px}
.net-weight strong{display:block;font-weight:400;font-size:21px;line-height:1.2}
.ring{position:absolute;left:278px;top:508px;width:270px;height:270px}
.origin-seal{position:absolute;left:430px;top:499px;width:80px;height:80px;border-radius:50%;border:4px solid var(--red);background:var(--paper)}
.french{position:absolute;left:283px;top:592px;color:var(--ink)}
.french__size{position:absolute;left:0;top:4px;font-family:'Oswald',sans-serif;font-weight:400;font-size:16px;line-height:18px;white-space:nowrap;letter-spacing:-.5px}
.french__sable{position:absolute;left:120px;top:-6px;font-family:'Playfair Display',serif;font-size:44px;white-space:nowrap}
.french__irish{position:absolute;left:-2px;top:30px;font-family:'Playfair Display',serif;font-size:62px;color:var(--plum);white-space:nowrap;letter-spacing:-1px}
.french__trad{position:absolute;left:-2px;top:93px;font-family:'Playfair Display',serif;font-size:37px;white-space:nowrap}
.ingredients{position:absolute;left:31px;top:449px;width:302px;font-family:'Oswald',sans-serif;font-weight:300;font-size:14.5px;line-height:17.2px;color:var(--ink);text-align:justify}
.maker{position:absolute;left:31px;top:662px;font-family:'Oswald',sans-serif;font-weight:300;font-size:17px;line-height:20px;color:var(--ink)}
.maker__lead{letter-spacing:.18em}
.maker__flag{display:inline-block;width:10px;height:10px;border-radius:50%;background:var(--red);margin-left:6px}
.brand--back{left:185px;top:655px;width:150px}
.brand--back .brand__name{font-size:44px}
.brand--back .brand__tag{font-size:6px;margin-top:8px}
.nutrition{position:absolute;left:350px;top:443px;width:190px;height:292px;background:var(--paper);border:1.5px solid #000;padding:4px 4px 0 4px;font-family:'Roboto',sans-serif;color:#000;font-size:9px;line-height:1.2}
.nutrition h2{font-size:17px;font-weight:900;line-height:19px}
.nutrition .serving{font-size:11.5px;line-height:13px;margin-top:2px}
.nutrition .row{display:flex;justify-content:space-between;align-items:baseline;padding:1px 0}
.nutrition .rule{border-top:1px solid #000}
.nutrition .rule--thick{border-top:3px solid #000}
.nutrition .indent{padding-left:9px}
.nutrition b{font-weight:900}
.nutrition .cal{font-size:12.5px;font-weight:900}
.nutrition .dv{font-size:7.5px;font-weight:700;text-align:right;line-height:9px}
.nutrition .foot{font-size:7px;line-height:9px;padding-top:3px}
</style>
</head>
<body>
<div class="canvas">

  <section class="panel panel--front" aria-label="Pouch front">
    <div class="wash wash--front" role="img" aria-label="Yellow, orange and green watercolour wash"></div>
    <div class="hang-hole"></div>

    <div class="brand brand--front">
      <div class="brand__name">Pembly’s</div>
      <div class="brand__tag">Irish Shortbread</div>
    </div>

    <div class="count-banner">
      <svg width="270" height="47" viewBox="0 0 270 47"><path d="M8 0H262L254 23L270 47H0L14 23Z" fill="var(--ink)"/></svg>
      <span>12 COOKIES BITE SIZE</span>
    </div>

    <h1>
      <span class="title title--top">TRADITIONAL</span>
      <span class="title title--mid">IRISH</span>
      <span class="title title--bottom">SHORTBREAD</span>
    </h1>

    <div class="claims-wash" role="img" aria-label="Red and magenta paint swatch"></div>
    <ul class="claims">
      <li>NO ADDITIVES</li>
      <li>NO ADDED PRESERVATIVES</li>
      <li>NO ADDED COLOURS</li>
      <li>ALL BUTTER</li>
    </ul>

    <div class="net-weight"><small>Net. Wet.</small><strong>144g</strong></div>

    <svg class="ring" viewBox="0 0 270 270"><circle cx="135" cy="135" r="126" fill="none" stroke="var(--gold)" stroke-width="9"/></svg>
    <div class="origin-seal"></div>

    <div class="french" lang="fr">
      <div class="french__size">12 BISCUIT TAILLE<br>DE MORSURE</div>
      <div class="french__sable">Sablé</div>
      <div class="french__irish">Irlandais</div>
      <div class="french__trad">Traditionnel</div>
    </div>
  </section>

  <section class="panel panel--back" aria-label="Pouch back">
    <div class="wash wash--back" role="img" aria-label="Yellow and green watercolour wash"></div>

    <p class="ingredients">Ingredient List: Enriched flour, Butter, Corn Starch, Icing Sugar, Vanilla Extract (Artificial flavour, skim milk, carrageenan, mono- and diglycerides, cellulose gum, polysorbate 80), Espresso Instant Coffee, Turmeric. <span lang="fr">Liste d'ingrédients : Farine enrichie, beurre, amidon de maïs modifié, sucre glace, extrait de vanille (arôme artificiel, lait écrémé, carraghénine, mono- et diglycérides, gomme de cellulose, polysorbate 80), café expresso instantané, curcuma.</span></p>

    <p class="maker"><span class="maker__lead">Manufactured by</span><br>Harbourline Food Inc<br>Marlow, PE, C0B2X0<br>Canada<span class="maker__flag"></span></p>

    <div class="brand brand--back">
      <div class="brand__name">Pembly’s</div>
      <div class="brand__tag">Irish Shortbread</div>
    </div>

    <div class="nutrition">
      <h2>Nutrition Facts<br>Valeur nutritive</h2>
      <p class="serving">Per 2 cookies (24 g)<br>pour 2 biscuit (24 g)</p>
      <div class="row rule" style="margin-top:2px"><span class="cal">Calories 120</span><span class="dv">% Daily Value*<br>% valeur quotidienne*</span></div>
      <div class="row rule--thick"><span><b>Fat / Lipides</b> 7 g</span><span>9 %</span></div>
      <div class="row indent"><span>Saturated / saturés 4.5 g</span><span>24 %</span></div>
      <div class="row indent"><span>+ Trans / trans 0.4 g</span><span></span></div>
      <div class="row rule"><span><b>Carbohydrate / Glucides</b> 12 g</span><span></span></div>
      <div class="row indent"><span>Fibre / Fibres 0 g</span><span>1 %</span></div>
      <div class="row indent"><span>Sugars / Sucres 1 g</span><span>1 %</span></div>
      <div class="row rule"><span><b>Protein / Protéines</b> 2 g</span><span></span></div>
      <div class="row rule"><span><b>Cholesterol / Cholestérol</b> 20 mg</span><span></span></div>
      <div class="row rule"><span><b>Sodium</b> 55 mg</span><span>2 %</span></div>
      <div class="row rule--thick"><span>Potassium 10 mg</span><span>0 %</span></div>
      <div class="row rule"><span>Calcium 0 mg</span><span>0 %</span></div>
      <div class="row rule"><span>Iron / Fer 0.5 mg</span><span>3 %</span></div>
      <p class="foot rule--thick">*5% or less is <b>a little</b> 15% or more is <b>a lot</b><br>*5% ou moins c’est <b>peu</b>, 15% ou plus c’est <b>beaucoup</b></p>
    </div>
  </section>

</div>
</body>
</html>
```